5 website banners (slides show)

We need 5 website sliding banners created for a website all about internet safety. The topics for each banner are:

Cyberbullying
Fraud
seniors
social networking

Sizes: 953 pixels x 281 pixels

I have stock images to use or feel free to use your own or one I can purchase from pixelvarro.example.

Industry/Entity Type

Internet

```html
<!DOCTYPE html>
<html lang="en">
<head>
<meta charset="utf-8">
<title>Social Networking Banner</title>
<link rel="stylesheet" href="https://fonts.googleapis.com/css2?family=Varela+Round&family=Open+Sans:wght@400&display=swap">
<style>
  :root {
    --canvas-bg: #ffffff;
    --texture-tone: #eeeeee;
    --title-band: #8a79ea;
    --title-band-shade: #6f5fd0;
    --subtitle-band: #f57ae0;
    --text-light: #ffffff;
    --photo-light: #f7f5f6;
    --photo-warm: #f6c9b4;
    --photo-cool: #c9d8f2;
    --photo-pink: #f2c3ea;
  }
  html, body {
    margin: 0;
    padding: 0;
    overflow: hidden;
    background: var(--canvas-bg);
  }
  .banner {
    position: relative;
    width: 1200px;
    height: 354px;
    overflow: hidden;
    background: var(--canvas-bg);
  }
  .banner__texture {
    position: absolute;
    left: 0;
    top: 0;
    width: 640px;
    height: 354px;
    background: linear-gradient(90deg, var(--texture-tone) 0%, rgba(238,238,238,0.5) 45%, rgba(255,255,255,0) 100%);
  }
  .banner__photo {
    position: absolute;
    left: 648px;
    top: 0;
    width: 552px;
    height: 354px;
    background:
      radial-gradient(ellipse at 30% 35%, var(--photo-warm) 0%, rgba(246,201,180,0) 45%),
      radial-gradient(ellipse at 60% 25%, var(--photo-pink) 0%, rgba(242,195,234,0) 40%),
      radial-gradient(ellipse at 85% 45%, var(--photo-cool) 0%, rgba(201,216,242,0) 40%),
      linear-gradient(180deg, var(--photo-light) 0%, #f1e4de 100%);
  }
  .banner__bands {
    position: absolute;
    left: 0;
    top: 0;
  }
  .banner__title,
  .banner__subtitle {
    position: absolute;
    margin: 0;
    color: var(--text-light);
    white-space: nowrap;
  }
  .banner__title {
    left: 87px;
    top: 124px;
    font-family: "Varela Round", sans-serif;
    font-size: 41px;
    font-weight: 400;
    line-height: 48px;
    letter-spacing: 0.3px;
  }
  .banner__subtitle {
    left: 88px;
    top: 197px;
    font-family: "Open Sans", sans-serif;
    font-size: 20px;
    line-height: 28px;
  }
</style>
</head>
<body>
  <div class="banner">
    <div class="banner__texture"></div>
    <div class="banner__photo" role="img" aria-label="Photo of raised hands holding colourful thumbs-up like signs"></div>
    <svg class="banner__bands" width="640" height="354" viewBox="0 0 640 354" aria-hidden="true">
      <polygon points="62,192 590,192 581,198 62,198" fill="var(--title-band-shade)" opacity="0.35"/>
      <polygon class="title-band" points="57,111 611,111 585,187 57,187" fill="var(--title-band)"/>
      <polygon class="subtitle-band" points="57,187 554,187 530,235 57,235" fill="var(--subtitle-band)"/>
    </svg>
    <h1 class="banner__title">Social Networking</h1>
    <p class="banner__subtitle">Lorem ipsum dolor sit amet consectetue</p>
  </div>
</body>
</html>
```